Brisco & Thorne Price List for Dealers

Looking for a 4 pages total including front and back of catalog. Looking for a PDF that we can upload to a printer for production. Full color, professional looking. We have uploaded our current price list, just need to have it look a little more updated. See our website BriscoandThorne.com for more info on us, see our competitor QuillanandRusk.com, see our vendors Tovarin.com, Lumbrel.com, Zenquor.com, Pilv.com

Target Market(s)

automotive dealers, selling aftermarket products. Sunroofs, leather interiors, seat heaters, convertible top repairs, interior work see BriscoandThorne.com for info, also see our competitors quillanandrusk.com . See our vendors Tovarin.com, Lumbrel.com, Zenquor.com, Pilv.com

Industry/Entity Type

Automotive

Font styles to use
Serif

Colors

Designer to choose colors to be used in the design.

Requirements
Must have
• Logo, phone number, fax number, web address and email address which is INFO@BRISCOANDTHORNE.COM
Nice to have
• just looking for a nice, professional price list/catalog to hand out at auto dealers who sell our product.

```html
<!DOCTYPE html>
<html lang="en">
<head>
<meta charset="utf-8">
<title>Brisco &amp; Thorne – Sunroof &amp; Leather Interiors Price List</title>
<link rel="stylesheet" href="https://fonts.googleapis.com/css2?family=Merriweather:wght@700;900&family=Nunito:wght@400;600&display=swap">
<style>
  :root {
    --navy: #26408b;
    --row-light: #c7c7e0;
    --row-grey: #a9a7b8;
    --rule: #7fb6dc;
    --ink: #2b2b2b;
    --paper: #ffffff;
    --outline: #1a1a1a;
  }
  * { margin: 0; padding: 0; box-sizing: border-box; }
  html, body { width: 776px; height: 1200px; overflow: hidden; background: var(--paper); }
  .price-page {
    position: relative;
    width: 776px;
    height: 1200px;
    font-family: "Nunito", sans-serif;
    color: var(--ink);
  }
  .section-title {
    position: absolute;
    left: 0; width: 100%;
    text-align: center;
    font-family: "Merriweather", serif;
    font-weight: 900;
    color: var(--navy);
    letter-spacing: 1px;
    line-height: 1;
  }
  .section-intro {
    position: absolute;
    left: 60px; width: 656px;
    text-align: center;
    font-size: 20px;
    line-height: 28px;
  }
  .price-table {
    position: absolute;
    left: 72px;
    width: 623px;
    border-collapse: collapse;
    font-size: 20px;
  }
  .price-table th {
    background: var(--navy);
    color: #fff;
    font-family: "Merriweather", serif;
    font-weight: 700;
    font-size: 20px;
    text-align: center;
  }
  .price-table td {
    text-align: center;
    vertical-align: middle;
    padding: 0 18px;
    line-height: 26px;
    border-top: 2px solid var(--rule);
  }
  .price-table td.item { width: 310px; border-right: 2px solid var(--navy); }
  .row-light td { background: var(--row-light); }
  .row-grey td { background: var(--row-grey); }

  .sunroof-title { top: 72px; font-size: 62px; }
  .sunroof-intro { top: 152px; }
  .sunroof-table { top: 262px; }

  .leather-title { top: 748px; font-size: 54px; }
  .leather-intro { top: 810px; }
  .leather-table { top: 883px; border: 2px solid var(--outline); }
  .leather-table td { border-top: 2px solid var(--outline); }
  .leather-table td.item { border-right: none; text-align: left; padding-left: 70px; }
  .leather-table td.price { text-align: left; padding-left: 80px; }
  .leather-table .row-option td { background: #cfd0e6; }
  .leather-table .row-option td.item { padding-left: 16px; }
</style>
</head>
<body>
<main class="price-page">

  <h1 class="section-title sunroof-title">SUNROOF</h1>
  <p class="section-intro sunroof-intro">Don't go to just anyone! We have been installing sunroofs Since 1973- Trust the Pros. All sunroofs come with a limited lifetime warranty.</p>

  <table class="price-table sunroof-table">
    <tr style="height:38px"><th colspan="2">Full Feature Auto-Close Sunroofs</th></tr>
    <tr class="row-light" style="height:38px"><td class="item">All Cars</td><td class="price">$995.00</td></tr>
    <tr class="row-light" style="height:38px"><td class="item">Vans and SUV's</td><td class="price">$1295.00</td></tr>
    <tr style="height:36px"><th colspan="2">Additional</th></tr>
    <tr class="row-grey" style="height:62px"><td class="item">Rerouting Overhead Air Vents</td><td class="price">add$100.00</td></tr>
    <tr class="row-light" style="height:44px"><td class="item">Vehicles with ridges on roof</td><td class="price">add $100.00</td></tr>
    <tr class="row-grey" style="height:42px"><td class="item">Overhead Consoles</td><td class="price">add$50.00</td></tr>
    <tr class="row-light" style="height:72px"><td class="item">Spoiler Sunroofs-External Sliding Glass</td><td class="price">$895.00</td></tr>
    <tr class="row-grey" style="height:66px"><td class="item">Spoiler Sunroofs-With Auto-Close</td><td class="price">$995.00</td></tr>
  </table>

  <h2 class="section-title leather-title">LEATHER INTERIORS</h2>
  <p class="section-intro leather-intro">Nothing Beats the Luxury of Leather. Backed by a 3 year/36,000 Mile Warranty!</p>

  <table class="price-table leather-table">
    <tr style="height:38px"><th colspan="2">Leather Packages</th></tr>
    <tr class="row-grey" style="height:34px"><td class="item">Two Row Seating</td><td class="price">$945.00</td></tr>
    <tr class="row-light" style="height:34px"><td class="item">Three Row Seating</td><td class="price">$1345.00</td></tr>
    <tr style="height:36px"><th colspan="2">Options</th></tr>
    <tr class="row-option" style="height:36px"><td class="item">Two Tone Color Combos add</td><td class="price">$100.00</td></tr>
  </table>

</main>
</body>
</html>
```